Commercial Piping Company Needs A Modern Business Card

We need a clean business card for our commercial pipe lining company. We would like to see a mock up in two color schemes: Black, Grey and Blue and Black, Grey and Orange. We are in the piping industry, but want a professional, clean and modern look to the card.

Industry/Entity Type

Plumbing

Contact Information for Business Card

Name: Mark Telford
Title: Managing Partner
Phone: 608.352.9174
Email: Mark@VeltaSpan.Net

Requirements
Must have
• Back Side Should Have a White Back Ground with Full Logo. Front I would like to see a couple lay outs for contact info. Also the final card will have rounded edges, so please take that into account for printing.
Nice to have
• Two Color Palette Examples
Should not have
• No need for an address line

```html
<!DOCTYPE html>
<html lang="en">
<head>
<meta charset="utf-8">
<title>VeltaSpan Business Card</title>
<link href="https://fonts.googleapis.com/css2?family=Montserrat:wght@400;600;700&display=swap" rel="stylesheet">
<style>
  :root {
    --stage: #2b2b2d;
    --paper: #ffffff;
    --ink: #111111;
    --muted: #9a9a9a;
    --ring: #ffffff;
  }
  * { margin: 0; padding: 0; box-sizing: border-box; }
  html, body { width: 1200px; height: 885px; overflow: hidden; background: var(--stage); }
  body { position: relative; font-family: "Montserrat", sans-serif; color: var(--ink); }

  .card {
    position: absolute;
    width: 520px;
    height: 297px;
    background: var(--paper);
    border-radius: 22px;
    overflow: hidden;
  }
  .card--back { left: 90px; top: 150px; }
  .card--front { left: 590px; top: 440px; }

  .brand { display: flex; align-items: center; gap: 12px; }
  .brand__dot { width: 52px; height: 52px; border-radius: 50%; background: var(--ink); flex: none; }
  .brand__name { font-size: 38px; font-weight: 600; letter-spacing: 1px; line-height: 1; }
  .brand__tag { font-size: 11.5px; font-weight: 600; letter-spacing: 1.4px; line-height: 1.3; margin-top: 4px; text-transform: uppercase; }

  .card--back .brand { position: absolute; left: 50%; top: 50%; transform: translate(-50%, -50%); }

  .card--front .brand { position: absolute; left: 28px; top: 40px; }
  .card--front .brand__name { font-size: 30px; }
  .card--front .brand__tag { font-size: 9.5px; }

  .accent { position: absolute; right: 0; top: 0; width: 300px; height: 297px; }

  .contact { position: absolute; left: 28px; bottom: 28px; }
  .contact__name { font-size: 17px; font-weight: 700; text-transform: uppercase; letter-spacing: 0.5px; }
  .contact__role { font-size: 12px; color: var(--muted); margin-bottom: 8px; }
  .contact__line { display: flex; align-items: center; gap: 8px; font-size: 12px; line-height: 1.6; }
  .contact__line svg { width: 12px; height: 12px; flex: none; }
</style>
</head>
<body>

  <section class="card card--back" aria-label="Card back">
    <div class="brand">
      <span class="brand__dot"></span>
      <div>
        <div class="brand__name">VELTASPAN</div>
        <div class="brand__tag">Pipe Restoration Solutions<br>Investigate • Plan • Deliver</div>
      </div>
    </div>
  </section>

  <section class="card card--front" aria-label="Card front">
    <svg class="accent" viewBox="0 0 300 297" aria-hidden="true">
      <path d="M130 0 H300 V210 Z" fill="#111111"/>
      <circle cx="175" cy="130" r="126" fill="#111111" stroke="#ffffff" stroke-width="2.5"/>
    </svg>

    <div class="brand">
      <div>
        <div class="brand__name">VELTASPAN</div>
        <div class="brand__tag">Pipe Restoration Solutions<br>Investigate • Plan • Deliver</div>
      </div>
    </div>

    <div class="contact">
      <div class="contact__name">Mark Telford</div>
      <div class="contact__role">Managing Partner</div>
      <div class="contact__line">
        <svg viewBox="0 0 12 12"><path d="M2 1h2.5l1 3-1.5 1a6 6 0 0 0 3 3l1-1.5 3 1V10a1 1 0 0 1-1 1A9 9 0 0 1 1 2a1 1 0 0 1 1-1z" fill="#111"/></svg>
        <span>608.352.9174</span>
      </div>
      <div class="contact__line">
        <svg viewBox="0 0 12 12"><rect x="0.5" y="2" width="11" height="8" rx="1" fill="#111"/><path d="M1 2.5 6 6.5 11 2.5" stroke="#fff" stroke-width="1" fill="none"/></svg>
        <span>Mark@VeltaSpan.Net</span>
      </div>
      <div class="contact__line">
        <svg viewBox="0 0 12 12"><circle cx="6" cy="6" r="5.5" fill="#111"/><path d="M0.5 6h11M6 0.5c-2.5 3-2.5 8 0 11M6 0.5c2.5 3 2.5 8 0 11" stroke="#fff" stroke-width="0.8" fill="none"/></svg>
        <span>www.VeltaSpan.Net</span>
      </div>
    </div>
  </section>

</body>
</html>
```